Re-design existing website and add products for sale.

Our current website is very basic and cluttered. (brightwillowcare.com.au)We want a modern looking website that is easy to navigate. We also want to start selling essential oils and crystal products, so there needs to be a separate page for this. Also needs to be easily edited as we need to change the monthly oracle card with the description. Would like calming colours as we are all about natural healing. Alongside the services listed there should be a button to book now which asks for their name, email, phone number ect. and adds it to the cart.

• Logo is still being designed, please leave a space for the logo which will basically be a lotus flower within a mandala.

```html
<!DOCTYPE html>
<html lang="en">
<head>
<meta charset="utf-8">
<title>Bright Willow Care</title>
<link href="https://fonts.googleapis.com/css2?family=Courgette&family=Fredoka:wght@500;600&family=Mulish:wght@400;600;700&display=swap" rel="stylesheet">
<style>
:root{
  --purple:#5a3a8e;
  --purple-deep:#4a2f78;
  --magenta:#b3215d;
  --lavender:#efe6fb;
  --lilac:#d9c6f2;
  --ink:#333;
  --muted:#777;
  --white:#fff;
  --card:#eeeeee;
}
*{box-sizing:border-box;margin:0;padding:0}
html,body{width:1200px;height:4455px;overflow:hidden}
body{font-family:"Mulish",sans-serif;color:var(--ink);background:var(--white);position:relative}
.script{font-family:"Courgette",cursive}
.btn{display:inline-block;background:var(--magenta);color:var(--white);border-radius:30px;font-family:"Courgette",cursive;font-size:22px;padding:14px 44px;white-space:nowrap}
.btn-flat{font-family:"Mulish",sans-serif;font-size:15px;font-weight:600;padding:10px 26px}

/* header */
.site-header{position:absolute;top:0;left:0;width:1200px;height:150px;z-index:3}
.site-header svg{position:absolute;top:0;left:0}
.brand{position:absolute;left:78px;top:46px;display:flex;align-items:center;gap:12px}
.brand-dot{width:40px;height:40px;border-radius:50%;background:var(--lilac)}
.brand-name{font-family:"Courgette",cursive;font-size:30px;color:var(--magenta);white-space:nowrap}
.top-bar{position:absolute;right:90px;top:10px;display:flex;gap:26px;align-items:center;font-size:14px;color:var(--magenta)}
.dot-icon{width:18px;height:18px;border-radius:50%;background:var(--purple)}
.main-nav{position:absolute;right:78px;top:62px;display:flex;gap:32px;font-size:16px;font-weight:600;color:var(--purple-deep)}
.main-nav .active{color:var(--magenta);border-bottom:2px solid var(--magenta);padding-bottom:6px}

/* hero */
.hero{position:absolute;top:110px;left:0;width:1200px;height:570px;background:radial-gradient(circle at 30% 45%,#6b4fb8 0%,#3b2a7a 40%,#1d1846 100%)}
.hero-photo{position:absolute;right:40px;top:30px;width:520px;height:540px;background:radial-gradient(ellipse at 50% 50%,#e9e4ef 0%,#bcb3cf 45%,rgba(60,45,110,0) 72%)}
.hero h1{position:absolute;left:78px;top:208px;width:420px;font-family:"Fredoka",sans-serif;font-weight:600;font-size:40px;line-height:1.28;color:var(--white)}
.hero .btn{position:absolute;left:78px;top:395px;font-size:20px;padding:12px 40px}
.hero-dots{position:absolute;left:560px;top:545px;display:flex;gap:8px}
.hero-dots span{width:10px;height:10px;border-radius:50%;background:#cfc6e8}
.hero-dots .on{background:var(--magenta)}

/* welcome */
.welcome{position:absolute;top:680px;left:0;width:1200px;height:585px;text-align:center}
.welcome-mark{position:absolute;left:545px;top:50px;width:110px;height:70px;border-radius:50% 50% 10px 10px;background:linear-gradient(#e4d6f7,#c4aee8)}
.welcome .kicker{position:absolute;top:140px;width:100%;font-size:26px;color:var(--magenta)}
.welcome h2{position:absolute;top:180px;width:100%;font-size:42px;font-weight:400;color:var(--purple)}
.welcome .copy{position:absolute;left:290px;top:262px;width:620px;font-size:13.5px;line-height:1.7;color:var(--muted)}
.welcome .copy p{margin-bottom:14px}
.welcome .btn{position:absolute;left:510px;top:482px}

/* services */
.services{position:absolute;top:1265px;left:0;width:1200px;height:895px;background:radial-gradient(circle at 50% 50%,#fbf7ff 0%,#e9daf9 45%,#c9acee 100%)}
.services h2{position:absolute;top:58px;width:100%;text-align:center;font-size:40px;font-weight:400;color:var(--magenta)}
.figure{position:absolute;left:400px;top:300px;width:400px;height:460px;background:radial-gradient(ellipse at 50% 55%,#5c3f95 0%,#5c3f95 42%,rgba(200,170,235,0) 70%)}
.svc{position:absolute;width:104px;height:104px;border-radius:50%;background:var(--white);box-shadow:0 4px 12px rgba(90,58,142,.15)}
.svc::after{content:"";position:absolute;left:34px;top:34px;width:36px;height:36px;border-radius:50%;border:3px solid var(--purple)}
.svc.hl{background:var(--magenta)}
.svc.hl::after{border-color:var(--white)}
.svc-label{position:absolute;font-size:14px;line-height:1.4;color:var(--ink);width:180px}
.svc-label.l{text-align:right}

/* band */
.call-band{position:absolute;top:2160px;left:0;width:1200px;height:190px;background:var(--purple)}
.call-band p{position:absolute;top:42px;width:100%;text-align:center;font-size:26px;color:var(--white)}
.call-band .btn{position:absolute;left:488px;top:100px;font-family:"Mulish",sans-serif;font-weight:700;font-size:26px;padding:8px 32px}

/* products */
.products{position:absolute;top:2350px;left:0;width:1200px;height:640px}
.products h2{position:absolute;top:70px;width:100%;text-align:center;font-size:40px;font-weight:400;color:var(--magenta)}
.product{position:absolute;top:140px;width:240px;height:376px;background:var(--card);text-align:center}
.bottle{position:absolute;left:92px;top:40px;width:56px;height:150px;border-radius:8px 8px 4px 4px;background:linear-gradient(#222 0 22%,#3b2d4f 22% 100%)}
.bottle.b2{background:linear-gradient(#222 0 22%,#1d1d1d 22% 100%)}
.product h3{position:absolute;top:230px;width:100%;font-size:18px;font-weight:400;color:var(--ink)}
.product p{position:absolute;top:262px;width:100%;font-size:13px;color:var(--muted)}
.product .btn{position:absolute;left:44px;top:298px}
.prod-dots{position:absolute;left:582px;top:555px;display:flex;gap:8px}
.prod-dots span{width:9px;height:9px;border-radius:50%;background:#ddd}
.prod-dots .on{background:var(--magenta)}

/* oracle */
.oracle{position:absolute;top:2990px;left:0;width:1200px;height:510px;background:linear-gradient(90deg,#eeeaf8,#f1eef8)}
.oracle h2{position:absolute;left:108px;top:80px;font-size:40px;font-weight:400;color:var(--magenta)}
.oracle .price{position:absolute;left:110px;top:145px;font-size:30px;font-weight:600;color:var(--ink)}
.oracle .copy{position:absolute;left:110px;top:205px;width:420px;font-size:14px;line-height:1.7;color:var(--muted)}
.oracle .copy p{margin-bottom:14px}
.oracle .btn{position:absolute;left:110px;top:358px}
.oracle-card{position:absolute;left:765px;top:115px;width:240px;height:330px;background:linear-gradient(135deg,#6a4b8c,#c6a17a 55%,#4e3a6a)}
.oracle-pattern{position:absolute;right:0;top:40px;width:200px;height:440px;background:linear-gradient(90deg,rgba(220,210,240,0),#e2dbf0)}

/* contact */
.contact{position:absolute;top:3500px;left:0;width:1200px;height:615px;background:linear-gradient(#f3eff7,#ddd3e8)}
.contact h2{position:absolute;top:50px;width:100%;text-align:center;font-size:40px;font-weight:400;color:var(--magenta)}
.contact .lead{position:absolute;top:112px;width:100%;text-align:center;font-size:15px;font-style:italic;font-weight:600;color:var(--ink)}
.field{position:absolute;left:362px;width:478px;height:52px;background:var(--white);border:1px solid #e3dced;font-size:14px;color:var(--muted);padding:16px}
.contact .btn{position:absolute;left:510px;top:495px;padding:12px 44px}

/* footer */
.site-footer{position:absolute;top:4115px;left:0;width:1200px;height:340px;background:var(--purple-deep);color:var(--white)}
.foot-brand{position:absolute;left:70px;top:120px;width:250px;text-align:center}
.foot-brand .brand-name{font-size:26px;color:var(--magenta)}
.foot-social{display:flex;gap:10px;justify-content:center;margin-top:18px}
.foot-social span{width:36px;height:36px;border-radius:50%;background:var(--white)}
.foot-col{position:absolute;top:40px}
.foot-col h4{font-size:18px;font-weight:600;margin-bottom:22px}
.foot-col li{list-style:none;font-size:13px;line-height:29px;display:flex;align-items:center;gap:10px}
.foot-col li::before{content:"";width:5px;height:5px;border-radius:50%;background:var(--magenta)}
.foot-col.contact-col li{line-height:1.5;margin-bottom:18px}
.foot-col.contact-col li::before{display:none}
.foot-col .underline{text-decoration:underline;font-weight:700}
.ico{flex:none}
.copyright{position:absolute;top:300px;width:100%;text-align:center;font-size:13px}
.foot-rule{position:absolute;left:60px;right:60px;top:282px;height:1px;background:rgba(255,255,255,.2)}
</style>
</head>
<body>

<header class="site-header">
  <svg width="1200" height="150" viewBox="0 0 1200 150" aria-hidden="true">
    <path d="M0 0H1200V118C1000 150 820 92 600 118S250 150 0 112Z" fill="#fff"/>
    <path d="M0 112C250 150 380 92 600 118S1000 150 1200 118V126C1000 158 820 100 600 126S250 158 0 120Z" fill="#b3215d"/>
  </svg>
  <div class="brand"><span class="brand-dot"></span><span class="brand-name">Bright Willow Care</span></div>
  <div class="top-bar">
    <span style="display:flex;gap:8px;align-items:center"><svg class="ico" width="18" height="16" viewBox="0 0 18 16"><path d="M1 2h3l2 8h9l2-6H5" fill="none" stroke="#b3215d" stroke-width="2"/><circle cx="7" cy="14" r="1.6" fill="#b3215d"/><circle cx="14" cy="14" r="1.6" fill="#b3215d"/></svg>My Cart</span>
    <span class="dot-icon"></span><span class="dot-icon"></span>
  </div>
  <nav class="main-nav">
    <span class="active">HOME</span><span>ABOUT</span><span>SERVICES</span><span>ESSENTIAL OILS</span><span>CRYSTAL PRODUCTS</span><span>CONTACT</span>
  </nav>
</header>

<section class="hero">
  <div class="hero-photo" role="img" aria-label="Woman in white seated in meditation pose against a glowing sacred-geometry backdrop"></div>
  <h1>Find Your True Self and Bring Balance to Your Life</h1>
  <span class="btn">Book Now</span>
  <div class="hero-dots"><span></span><span class="on"></span><span></span><span></span></div>
</section>

<section class="welcome">
  <div class="welcome-mark" role="img" aria-label="Soft lavender lotus flower ornament"></div>
  <p class="kicker script">Welcome To</p>
  <h2 class="script">Bright Willow Care</h2>
  <div class="copy">
    <p>Are you struggling through life, feeling stuck, not feeling yourself, or simply feeling drained? Need to find a way to relax and rejuvenate, a way to free up your energy to work on that which better serves you in this lifetime?</p>
    <p>Working together with you, I can help you achieve this. Whether through spiritual healing sessions using Reiki and Seichim, through Oracle Card Readings or a combination of these.</p>
    <p>I am passionate about using my knowledge and skills to help others struggling through their life journey.</p>
  </div>
  <span class="btn">Learn More</span>
</section>

<section class="services">
  <h2 class="script">Our Services</h2>
  <div class="figure" role="img" aria-label="Purple silhouette of a meditating figure with glowing chakra points on a lotus"></div>

  <div class="svc" style="left:468px;top:168px"></div>
  <div class="svc-label l" style="left:270px;top:195px">Crystals &amp; Hand Made Jewellery Available</div>
  <div class="svc hl" style="left:325px;top:273px"></div>
  <div class="svc-label l" style="left:130px;top:300px">Reiki &amp; Seichim Workshops</div>
  <div class="svc" style="left:236px;top:406px"></div>
  <div class="svc-label l" style="left:40px;top:433px">Reiki &amp; Seichim Healings</div>
  <div class="svc" style="left:200px;top:545px"></div>
  <div class="svc-label l" style="left:6px;top:572px">Energy Balancing</div>
  <div class="svc" style="left:209px;top:688px"></div>
  <div class="svc-label l" style="left:16px;top:715px">Energy Healing</div>

  <div class="svc" style="left:622px;top:168px"></div>
  <div class="svc-label" style="left:758px;top:195px">Oracle Card Readings /Online Readings</div>
  <div class="svc" style="left:750px;top:273px"></div>
  <div class="svc-label" style="left:880px;top:300px">Essential Oil Roll On Blends Available</div>
  <div class="svc" style="left:848px;top:400px"></div>
  <div class="svc-label" style="left:975px;top:427px">Distant Healing</div>
  <div class="svc" style="left:883px;top:540px"></div>
  <div class="svc-label" style="left:1008px;top:567px">Past Life Clearing</div>
  <div class="svc" style="left:883px;top:698px"></div>
  <div class="svc-label" style="left:1008px;top:725px">Chakra Balancing</div>
</section>

<section class="call-band">
  <p class="script">Find Your True Self and Bring Balance to Your Life</p>
  <span class="btn">0400 123 456</span>
</section>

<section class="products">
  <h2 class="script">Our Products</h2>
  <article class="product" style="left:80px"><div class="bottle" role="img" aria-label="Essential oil bottle"></div><h3>ESSENTIAL OILS</h3><p>Lorem ipsum simple text print.</p><span class="btn btn-flat">ADD TO CART</span></article>
  <article class="product" style="left:347px"><div class="bottle b2" role="img" aria-label="Essential oil bottle"></div><h3>ESSENTIAL OILS</h3><p>Lorem ipsum simple text print.</p><span class="btn btn-flat">ADD TO CART</span></article>
  <article class="product" style="left:614px"><div class="bottle" role="img" aria-label="Essential oil bottle"></div><h3>ESSENTIAL OILS</h3><p>Lorem ipsum simple text print.</p><span class="btn btn-flat">ADD TO CART</span></article>
  <article class="product" style="left:881px"><div class="bottle b2" role="img" aria-label="Essential oil bottle"></div><h3>ESSENTIAL OILS</h3><p>Lorem ipsum simple text print.</p><span class="btn btn-flat">ADD TO CART</span></article>
  <div class="prod-dots"><span></span><span class="on"></span></div>
</section>

<section class="oracle">
  <div class="oracle-pattern" role="img" aria-label="Faint lavender damask ornament"></div>
  <h2 class="script">Oracle Card Readings</h2>
  <p class="price">20 Min - $30</p>
  <div class="copy">
    <p>Oracle cards, also known as wisdom cards are cards used for divination, fortune telling and spiritual guidance.</p>
    <p>Oracle cards are the modern version of tarot cards, which have been used for centuries by people to find meaningful answers to questions about their life, spiritual path and future.</p>
  </div>
  <span class="btn">Get Started</span>
  <div class="oracle-card" role="img" aria-label="Boxed oracle card deck of the month"></div>
</section>

<section class="contact" aria-label="Contact form over a soft photo of a woman with raised arms">
  <h2 class="script">Get In Touch</h2>
  <p class="lead">If you Need An have any question Pls fill up the form.</p>
  <div class="field" style="top:150px">Name *</div>
  <div class="field" style="top:215px">Email *</div>
  <div class="field" style="top:280px">Phone *</div>
  <div class="field" style="top:345px">Services *</div>
  <div class="field" style="top:410px;height:70px">Message *</div>
  <span class="btn">Submit</span>
</section>

<footer class="site-footer">
  <div class="foot-brand">
    <div class="brand-name">Bright Willow Care</div>
    <div class="foot-social"><span></span><span></span><span></span></div>
  </div>
  <div class="foot-col" style="left:345px">
    <h4>Site Map</h4>
    <ul><li>Home</li><li>About</li><li>Services</li><li>Essential Oils</li><li>Crystal Products</li><li>Contact</li></ul>
  </div>
  <div class="foot-col" style="left:609px">
    <h4>Services</h4>
    <ul><li>Reiki &amp; Seichim Healings</li><li>Energy Healing</li><li>Chakra Balancing</li><li>Energy Balancing</li><li>Past Life Clearing</li><li class="underline">View More</li></ul>
  </div>
  <div class="foot-col contact-col" style="left:876px">
    <h4>Contact Us</h4>
    <ul>
      <li><svg class="ico" width="16" height="16" viewBox="0 0 16 16"><path d="M3 1l3 3-2 2c1 2 3 4 5 5l2-2 3 3-2 3C6 14 2 10 1 3z" fill="#b3215d"/></svg>0400 123 456</li>
      <li><svg class="ico" width="14" height="18" viewBox="0 0 14 18"><path d="M7 0a7 7 0 0 0-7 7c0 5 7 11 7 11s7-6 7-11a7 7 0 0 0-7-7z" fill="#b3215d"/><circle cx="7" cy="7" r="2.5" fill="#4a2f78"/></svg>12 Willow Lane<br>Northfield, SA 5085</li>
      <li><svg class="ico" width="18" height="14" viewBox="0 0 18 14"><rect width="18" height="14" rx="2" fill="#b3215d"/><path d="M1 2l8 6 8-6" fill="none" stroke="#4a2f78" stroke-width="1.5"/></svg>hello@brightwillowcare.com.au</li>
    </ul>
  </div>
  <div class="foot-rule"></div>
  <p class="copyright">©Bright Willow Care - 2019 All Right Reserved.</p>
</footer>

</body>
</html>
```